Business Card for Pet Food Deliver

Looking for a business card design for a start up company. We are Brisk Hound, Premium Pet Products Brought Round.

We market and are designing a website where our clients can go to and order pet food. We then deliver to a local client base. We do person to person deliver, we do not ship at this point. We are starting off with dog and cat food and treats.

Attached is our logo. We are looking for a fun yet professional design. Eye catching with color but not over the top with color. Looking for a double sided card. Contact info on the front and our logo on the back maybe. . .

I am a huge green fan. However, I am thinking I like the orange a bit more then the blue and green for dominant colors. . .

I am attaching our logo.

The file that has our slogan under has a minor change not implemented yet. The word 'Premium' should be gray to match and the word 'Delivered' should be black to match.

Target Market(s)

We are looking to service those pet owners looking for the convenience of not having to drive to a pet store to purchase their products. We are looking for those who are web savvy and purchase online.

We will also be targeting seniors in senior communities without consistent transprotation.

Industry/Entity Type

Pet

Font styles to use
Sans Serif

Colors
f37122
3176b5
acd036

Requirements
Must have
• Double sided. Logo only on one side with a bold color for the background.

Space for name, phone number, website address, mailing address.
Should not have
• No paws, delivery trucks.

```html
<!DOCTYPE html>
<html lang="en">
<head>
<meta charset="utf-8">
<title>Brisk Hound – Business Card</title>
<link rel="stylesheet" href="https://fonts.googleapis.com/css2?family=Open+Sans:wght@400;700&display=swap">
<style>
  :root {
    --page: #e9e6e2;
    --card-white: #ffffff;
    --orange: #f18e00;
    --green: #a2c532;
    --blue: #38a9de;
    --logo-grey: #9a9a9a;
    --tag-light: #c4c4c4;
    --tag-dark: #8a8a8a;
    --ink-white: #ffffff;
  }
  * { margin: 0; padding: 0; box-sizing: border-box; }
  html, body { width: 1200px; height: 1000px; overflow: hidden; }
  body {
    background: var(--page);
    font-family: "Open Sans", Arial, sans-serif;
    position: relative;
  }
  .card {
    position: absolute;
    left: 190px;
    width: 820px;
    height: 430px;
    border-radius: 38px;
    overflow: hidden;
    box-shadow: 0 6px 18px rgba(0,0,0,0.18);
  }
  /* Logo side */
  .card-logo { top: 40px; background: var(--card-white); }
  .brand-lockup {
    position: absolute;
    left: 160px; top: 130px;
    display: flex; align-items: center; gap: 26px;
  }
  .brand-dot {
    width: 90px; height: 90px; border-radius: 50%;
    background: var(--logo-grey);
  }
  .brand-name {
    font-size: 76px; font-weight: 400; color: var(--logo-grey);
    line-height: 1; letter-spacing: -1px;
  }
  .brand-tagline {
    margin-top: 10px;
    font-size: 30px; font-weight: 700; line-height: 1;
  }
  .brand-tagline .premium { color: var(--tag-light); }
  .brand-tagline .brought { color: var(--tag-dark); }
  .accent-stripe {
    position: absolute; left: 0; right: 0; bottom: 44px; height: 7px;
    display: flex;
  }
  .accent-stripe span { flex: 1; }
  .accent-stripe .s-orange { background: var(--orange); }
  .accent-stripe .s-green { background: var(--green); }
  .accent-stripe .s-blue { background: var(--blue); }

  /* Contact side */
  .card-contact { top: 530px; display: flex; color: var(--ink-white); }
  .band { flex: 1; height: 100%; }
  .band-orange { background: var(--orange); }
  .band-green { background: var(--green); }
  .band-blue { background: var(--blue); }
  .contact-layer { position: absolute; inset: 0; }
  .company-line {
    position: absolute; top: 40px; right: 80px;
    font-size: 32px; white-space: nowrap;
  }
  .company-line b { font-weight: 700; }
  .person-line {
    position: absolute; top: 190px; left: 70px;
    font-size: 34px; white-space: nowrap;
  }
  .person-line b { font-weight: 700; }
  .footer {
    position: absolute; left: 70px; bottom: 40px;
    display: flex; align-items: flex-end; gap: 20px;
    font-size: 19px; line-height: 1.35;
  }
  .footer-name { font-size: 15px; font-weight: 700; padding-bottom: 4px; }
  .address { text-align: right; padding-right: 18px; border-right: 1px solid rgba(255,255,255,0.8); }
  .contacts { list-style: none; }
  .contacts li { display: flex; align-items: center; gap: 6px; }
  .contacts svg { width: 17px; height: 17px; flex: none; }
</style>
</head>
<body>

<section class="card card-logo" aria-label="Business card, logo side">
  <div class="brand-lockup">
    <div class="brand-dot"></div>
    <div>
      <div class="brand-name">Brisk Hound</div>
      <div class="brand-tagline"><span class="premium">Premium</span> <span class="brought">Brought Round</span></div>
    </div>
  </div>
  <div class="accent-stripe">
    <span class="s-orange"></span><span class="s-green"></span><span class="s-blue"></span>
  </div>
</section>

<section class="card card-contact" aria-label="Business card, contact side">
  <div class="band band-orange"></div>
  <div class="band band-green"></div>
  <div class="band band-blue"></div>
  <div class="contact-layer">
    <p class="company-line"><b>BRISK HOUND</b> PREMIUM BROUGHT ROUND</p>
    <p class="person-line"><b>Daniel Harrow</b> Nutrition Specialist</p>
    <div class="footer">
      <div class="footer-name">Brisk Hound</div>
      <div class="address">Address<br>2207 Alder Crest Lane<br>Fenwick, WI 54921</div>
      <ul class="contacts">
        <li><svg viewBox="0 0 16 16" fill="none" stroke="#fff" stroke-width="1.4"><rect x="4" y="1" width="8" height="14" rx="1.5"/><line x1="7" y1="12.5" x2="9" y2="12.5"/></svg>555-014-27</li>
        <li><svg viewBox="0 0 16 16" fill="none" stroke="#fff" stroke-width="1.4"><rect x="1" y="3" width="14" height="10"/><polyline points="1,3 8,9 15,3"/></svg>hello@briskhound.com</li>
        <li><svg viewBox="0 0 16 16" fill="none" stroke="#fff" stroke-width="1.3"><circle cx="8" cy="8" r="6.5"/><ellipse cx="8" cy="8" rx="3" ry="6.5"/><line x1="1.5" y1="8" x2="14.5" y2="8"/></svg>www.BriskHoundBrings.com</li>
      </ul>
    </div>
  </div>
</section>

</body>
</html>
```